Web Design Project

Brightwater Digital owns and operates a large number of editorial websites. These websites provides mostly consumers in the financial services space with information and price comparisons for a particular service.

Brightwater Digital, as the holding company for each of these sites, currently has no website. We need to build a website targeted towards potential partners for our websites. The idea being that when we start a conversation with a partner, they can view our site and obtain some basic information about who we are.

The structure of the site is to be very simple, containing only a brief description about who we are, our contact details and a list of some of our websites:
• CoverQuest.net.au
• AutoPolicyMatcher.com.au
• NestPolicyMatcher.com.au
• WellPolicyMatcher.com.au
• CoverQuestMatcher.com.au
• TripPolicyMatcher.com.au
• CritterPolicyMatcher.com.au
• CashAdvanceMatcher.com.au
• MobileCoolingUnit.com.au
• FixedSaverYields.com.au
• ThriftyHabits.com.au
• PurseGran.com.au
• TameThePlastic.com.au
• PurseMinder.com.au
• ThirdPartyClaimsCoverOzland.com.au
• Trade-Protect.com.au
• AutoPolicyProviders.com.au
• WellPolicyProviders.com.au
• NestPolicyOzland.com
• CoverQuestOzland.com
• WageShieldPolicyOzland.com
• WellPolicyOzland.com
• CritterPolicyOzland.com
• CashAdvancesOzland.com
• PlasticPaysOzland.com
• NestLendersOzland.com
• NestEggFunds.net.au

The design of the site should say 'Internet company', 'professional', 'fresh thinking'. The design should not look like a corporate site that you would see from any corporate services business with images of people in suits. We are ultimately an Internet business and there should be a unique feel to the site.

We are open to a suggestion of a colour pallet as the holding company does not have an established logo.

Some sites that we like are:

http://www.prismwork-studio.co.uk/#home
http://sample00.layoutvault.example/wt_48248/index.html
http://sample00.layoutvault.example/wordpress_46388/
http://mindvolt.example/
http://www.tandora.us/
http://www.kelvorabintu.example/
http://www.slickfrontpages.example/Corporate/design-ideas-detail.html?id=7916
http://trebla.example/
http://orvantek.example/

Reason: Hi all, Apologies, but I need to extend the timeline. One of our key stakeholders is away for the next week. There are a few good designs that we have received to date and there are some tweaks that we would like to see before making a final decision. Thank you to everyone that has submitted designs - Have a great new year. Derek

Reason: Sorry to have to delay the deadline on this, but we did not find anything in the designs really resonated with us. We will have a further think about the existing designs that have been submitted and how we can provide more specific feedback to the designers to make some modifications to the designs.

Target Market(s)

We are targeting insurance companies / brokers that we are talking to. The idea is that we show a professional face to them.

Industry/Entity Type

Financial

Requirements
Must have
• Home Page (possibly integrated with About us details)
Contact Us
Our Sites

```html
<!DOCTYPE html>
<html lang="en">
<head>
<meta charset="utf-8">
<title>Brightwater Digital</title>
<link rel="stylesheet" href="https://fonts.googleapis.com/css2?family=Arimo:wght@400;700&family=Great+Vibes&display=swap">
<style>
:root{
  --green:#77a50b;
  --green-light:#c6e85a;
  --dark:#232323;
  --band:#3a3a3a;
  --tab:#1e1e1e;
  --panel:#ededed;
  --text:#6a6a6a;
  --ink:#222;
  --footer:#ececec;
}
*{box-sizing:border-box;margin:0;padding:0}
html,body{width:1200px;height:1010px;overflow:hidden}
body{position:relative;background:#fff;font-family:'Arimo',Arial,sans-serif;color:var(--text)}
.abs{position:absolute}
.band-top{left:0;top:0;width:1200px;height:108px;background:var(--dark)}
.band-mid{left:0;top:108px;width:1200px;height:292px;background:var(--band)}
.header{left:176px;top:17px;width:861px;height:91px;background:var(--band);border-radius:4px 4px 0 0}
.logo{left:190px;top:46px;font-size:38px;color:#fff;font-weight:400;letter-spacing:-.3px;white-space:nowrap}
.nav a{position:absolute;top:52px;height:48px;width:131px;color:#fff;font-size:14px;text-align:center;line-height:58px;text-decoration:none;background:var(--tab);border-radius:4px 4px 0 0}
.nav a.active{background:var(--green)}
.hero{left:176px;top:100px;width:862px;height:308px;background:var(--green);border-radius:0 4px 4px 4px}
.hero-card{left:184px;top:107px;width:564px;height:291px;background:linear-gradient(90deg,#fff 55%,#ececec);border-radius:6px;overflow:hidden}
.hero-photo{left:0;top:0;width:290px;height:291px;background:radial-gradient(circle at 45% 50%,#9a9a9a,#d8d8d8 55%,#f7f7f7)}
.hero-lead{left:296px;top:47px;width:222px;font-size:12.5px;font-style:italic;color:var(--ink);line-height:17.5px}
.hero-body{left:296px;top:121px;width:222px;font-size:12.5px;color:#8a8a8a;line-height:17.5px}
.hero-rule{left:296px;top:232px;width:220px;height:1px;background:#cfcfcf}
.read-more{left:437px;top:241px;width:80px;height:22px;background:linear-gradient(#fff,#e6e6e6);border:1px solid #d4d4d4;border-radius:3px;font-size:11px;color:var(--green);text-align:center;line-height:20px;font-weight:700}
.feature-top{left:748px;top:163px;width:229px;height:37px;background:#fff;border-radius:0 3px 3px 0;font-size:11px;letter-spacing:-.2px;white-space:nowrap;color:var(--ink);padding:13px 0 0 4px}
.feature{position:absolute;left:754px;width:274px;height:37px;background:linear-gradient(#fff,#ececec);border-radius:3px;font-size:10.8px;letter-spacing:-.25px;white-space:nowrap;overflow:hidden;color:var(--ink);display:flex;align-items:center}
.feature svg{width:40px;height:37px;flex:none;border-right:1px solid #ddd;margin-right:4px}
.col{top:423px;width:283px;background:var(--panel);border-radius:5px}
.col h2{height:53px;font-weight:400;font-size:21px;color:#fff;padding:16px 0 0 17px;background:var(--green);border-radius:5px 5px 0 0;white-space:nowrap}
.col-insurance h2{background:linear-gradient(#4a4a4a,#111);padding-left:7px;font-size:19px;letter-spacing:-.2px;padding-top:17px}
.col-insurance p{font-size:11.5px;line-height:24px;text-align:justify;padding:0 17px 0 15px}
.col-insurance .sub{font-weight:700;color:#666}
.col-insurance .intro{padding-top:7px}
.articles{list-style:none;padding:4px 0 0 18px}
.articles li{font-size:13.5px;line-height:27px;color:#707070;padding-left:28px;position:relative;white-space:nowrap}
.articles li::before{content:"";position:absolute;left:2px;top:9px;border-left:7px solid #b9d46a;border-top:5px solid transparent;border-bottom:5px solid transparent}
.welcome p{font-size:11.5px;line-height:24px;padding:5px 14px 0 17px}
.shadow{height:10px;background:radial-gradient(ellipse at 50% 0,rgba(0,0,0,.45),rgba(0,0,0,0) 70%)}
.quote-box{left:465px;top:760px;width:409px;height:117px;border:1px solid #333;border-radius:4px;background:linear-gradient(#fff,#ececec)}
.quote-title{left:517px;top:728px;font-family:'Great Vibes',cursive;font-size:50px;color:var(--green);white-space:nowrap}
.quote-label{left:465px;top:792px;width:409px;text-align:center;font-size:21px;color:#333}
.quote-input{left:591px;top:826px;width:113px;height:34px;border:1px solid #bbb;border-radius:6px;background:#f3f3f3}
.quote-go{left:713px;top:820px;font-family:'Great Vibes',cursive;font-size:30px;color:var(--green);text-decoration:underline}
.news-box{left:880px;top:760px;width:156px;height:117px;border:1px solid #333;border-radius:4px;background:linear-gradient(#fff,#ececec)}
.news-text{left:880px;top:828px;width:156px;text-align:center;font-size:16px;line-height:20px;color:#222}
.footer{left:0;top:909px;width:1200px;height:80px;background:var(--footer)}
.footer-base{left:0;top:989px;width:1200px;height:21px;background:var(--band)}
.copy{right:181px;top:920px;font-size:13px;color:#222;white-space:nowrap}
.foot-nav{right:176px;top:954px;font-size:13.5px;color:var(--green);white-space:nowrap}
.foot-nav span{color:#666;margin:0 18px}
.foot-nav .on{text-decoration:underline}
</style>
</head>
<body>
<div class="abs band-top"></div>
<div class="abs band-mid"></div>
<div class="abs header"></div>
<div class="abs logo">Brightwater Digital</div>
<nav class="nav">
  <a class="active" style="left:501px">Home</a>
  <a style="left:635px">About Us</a>
  <a style="left:768px">Contact Us</a>
  <a style="left:901px">Our Sites</a>
</nav>

<div class="abs hero"></div>
<div class="abs hero-card">
  <div class="abs hero-photo" role="img" aria-label="Photo of several black and silver computer mice on a white background"></div>
  <p class="abs hero-lead">Vivamus sed urna. Nunc lorem. Pellentesque mattis pharetra nim. Vivamus quis nulla a sapien pel lentesque congue.</p>
  <p class="abs hero-body">Pellentesque mattis pharetra nim. Vivamus quis nulla a sapien pellen tesque congue. Fusce a diam ac felis eleifend. viverra. Etiam porta consequat nulla. Mauris ipsum lorem mattis vel interdum id.</p>
  <div class="abs hero-rule"></div>
  <div class="abs read-more">READ MORE</div>
</div>
<div class="abs feature-top">The “When” in Life Insurance: The Big Plan</div>
<div class="feature" style="top:202px"><svg viewBox="0 0 40 37"><circle cx="20" cy="18" r="11" fill="#3bb7e8"/><path d="M20 18V7A11 11 0 0 1 31 18Z" fill="#e6f6fb"/></svg>Life Insurance Coverage:The Right Amount</div>
<div class="feature" style="top:242px"><svg viewBox="0 0 40 37"><path d="M13 28V16a7 7 0 0 1 14 0v12h-4V16a3 3 0 0 0-6 0v12Z" fill="#d23a2a"/></svg>The “When” in Life Insurance: Don’t miss out</div>
<div class="feature" style="top:281px"><svg viewBox="0 0 40 37"><circle cx="20" cy="18" r="11" fill="#f2b721"/><circle cx="20" cy="18" r="7" fill="none" stroke="#c88a08"/></svg>Purchasing Team Life Insurance:Tips</div>
<div class="feature" style="top:320px"><svg viewBox="0 0 40 37"><circle cx="20" cy="18" r="11" fill="#f4f4f4" stroke="#555" stroke-width="1.5"/><path d="M20 18V10" stroke="#333" stroke-width="1.5"/></svg>Shopping for life insurance in Australia</div>
<div class="feature" style="top:360px"><svg viewBox="0 0 40 37"><rect x="15" y="7" width="10" height="9" fill="#f59b1c"/><rect x="9" y="17" width="10" height="9" fill="#f59b1c"/><rect x="21" y="17" width="10" height="9" fill="#f59b1c"/></svg>Shopping for life insurance in Australia</div>

<section class="abs col col-insurance" style="left:176px;height:463px">
  <h2>What Type Of Insurance Is Best</h2>
  <p class="intro">Choosing which type of insurance is best for you is not always an easy decision. There are many factors that you must consider such as age and family expenses. First let's break down the 3 most popular options available; Term, Whole Life, and Universal.</p>
  <p class="sub">Term Life Insurance</p>
  <p>A term life insurance policy pays out a death benefit only if the person covered dies during the specified term. For example, if you take out a term life insurance policy you might take it out for ten years, or it might be dependent upon the insured individual becoming a certain age. You cannot cash out a term life policy; instead, the policy pays a lump sum to any dependents upon death.</p>
</section>
<div class="abs shadow" style="left:186px;top:886px;width:263px"></div>

<section class="abs col" style="left:464px;height:281px">
  <h2>Recent Articles</h2>
  <ul class="articles">
    <li>Life Insurance for Children</li>
    <li>Life Insurance for Seniors</li>
    <li>Life Insurance &nbsp;Stay At Home Mother</li>
    <li>Life Insurance Case Studies</li>
    <li>Life Insurance in Estate Planning</li>
    <li>Life Insurance for Seniors</li>
    <li>Life Insurance Case Studies</li>
    <li>Life Insurance in Estate Planning</li>
  </ul>
</section>
<div class="abs shadow" style="left:474px;top:704px;width:263px"></div>

<section class="abs col welcome" style="left:752px;height:281px">
  <h2>Welcome!</h2>
  <p>Lorem Ipsum is simply dummy text of the printing and typesetting industry. Lorem Ipsum has been the industry's standard dummy text ever since the 1500s, when an unknown printer took a galley of type and scrambled it to make a type specimen book. It has survived not only five centuries, but also the leap into electronic typesetting, remaining essentially unchanged.</p>
</section>
<div class="abs shadow" style="left:762px;top:704px;width:263px"></div>

<div class="abs quote-box"></div>
<div class="abs quote-title">Get A Quote Now !</div>
<div class="abs quote-label">Enter your Post Code:</div>
<div class="abs quote-input"></div>
<div class="abs quote-go">Go!</div>

<div class="abs news-box"></div>
<svg class="abs" style="left:886px;top:771px" width="36" height="36" viewBox="0 0 36 36" aria-hidden="true">
  <rect x="1" y="1" width="34" height="34" rx="6" fill="#f28a1e" stroke="#c8650c"/>
  <circle cx="10" cy="26" r="3" fill="#fff"/>
  <path d="M8 17a11 11 0 0 1 11 11M8 10a18 18 0 0 1 18 18" fill="none" stroke="#fff" stroke-width="3.5"/>
</svg>
<div class="abs news-text">Get the latest news<br>&amp; updates</div>

<footer>
  <div class="abs footer"></div>
  <div class="abs copy">Brightwater Digital © 2011 &nbsp;&nbsp; I &nbsp;&nbsp; Privacy Policy</div>
  <div class="abs foot-nav"><span class="on" style="margin:0;color:var(--green)">About us</span><span>I</span>Solutions<span>I</span>Projects<span>I</span>Contacts</div>
  <div class="abs footer-base"></div>
</footer>
</body>
</html>
```